Design for Certificate

Design a certificate for training, providing our company logo such as attachments. Company's name is "ØSTRA Velmark Advisory Ltd", please refer to our company profile: https://www.ostra-velmark.example/company_info

The style of the current certificate is also attached, and another certificate of another company can be referred to. Psd & jpg are required for the final draft (the layers of psd are not merged). Thanks!

```html
<!DOCTYPE html>
<html lang="en">
<head>
<meta charset="utf-8">
<title>Certificate of Completion – ØSTRA Velmark Advisory Ltd</title>
<link href="https://fonts.googleapis.com/css2?family=Cormorant+Garamond:ital,wght@0,600;1,500;1,600&family=Pinyon+Script&family=Playfair+Display:ital,wght@1,900&display=swap" rel="stylesheet">
<style>
  :root {
    --paper: #f7f7f7;
    --gold: #dbb55e;
    --charcoal: #484745;
    --ink: #46443f;
    --rule: #6b6a67;
    --white: #ffffff;
  }
  * { margin: 0; padding: 0; box-sizing: border-box; }
  html, body { width: 1200px; height: 846px; overflow: hidden; background: var(--paper); }
  .certificate {
    position: relative;
    width: 1200px;
    height: 846px;
    background: var(--paper);
    overflow: hidden;
  }
  .frame-lines { position: absolute; inset: 0; }
  .corner-flourish {
    position: absolute;
    width: 46px;
    height: 46px;
    background: radial-gradient(circle at 30% 30%, rgba(219,181,94,.55), rgba(219,181,94,0) 70%);
  }
  .corner-flourish.tl { left: 8px; top: 8px; }
  .corner-flourish.tr { right: 8px; top: 8px; transform: scaleX(-1); }
  .corner-flourish.bl { left: 8px; bottom: 8px; transform: scaleY(-1); }
  .corner-flourish.br { right: 8px; bottom: 8px; transform: scale(-1,-1); }

  .brand-band {
    position: absolute;
    left: 93px;
    top: 0;
    width: 249px;
    height: 846px;
    background: var(--charcoal);
  }
  .brand-name {
    position: absolute;
    left: 0;
    right: 0;
    top: 680px;
    text-align: center;
    font-family: "Cormorant Garamond", Georgia, serif;
    font-weight: 600;
    color: var(--white);
    line-height: 1.05;
  }
  .brand-name span { display: block; }
  .brand-name .line-1 { font-size: 58px; letter-spacing: 10px; margin-right: -10px; }
  .brand-name .line-2 { font-size: 38px; letter-spacing: 3px; margin-right: -3px; }

  .content {
    position: absolute;
    left: 430px;
    width: 666px;
    top: 0;
    height: 846px;
    text-align: center;
    color: var(--ink);
  }
  .title {
    position: absolute;
    top: 88px;
    left: 0; right: 0;
    font-family: "Playfair Display", Georgia, serif;
    font-style: italic;
    font-weight: 900;
    font-size: 42px;
    color: var(--gold);
    word-spacing: 22px;
    letter-spacing: -1px;
  }
  .lead {
    font-family: "Cormorant Garamond", Georgia, serif;
    font-style: italic;
    font-weight: 600;
    font-size: 33px;
    position: absolute;
    left: 0; right: 0;
  }
  .lead.awarded { top: 198px; }
  .lead.completed { top: 383px; font-size: 31px; }
  .recipient-line {
    position: absolute;
    top: 362px;
    left: 100px;
    width: 465px;
    border-top: 1px solid var(--rule);
  }
  .course {
    position: absolute;
    top: 436px;
    left: 0; right: 0;
    font-family: "Cormorant Garamond", Georgia, serif;
    font-style: italic;
    font-weight: 500;
    font-size: 48px;
    color: var(--gold);
  }
  .duration {
    position: absolute;
    top: 534px;
    left: 0; right: 0;
    font-family: "Cormorant Garamond", Georgia, serif;
    font-style: italic;
    font-weight: 600;
    font-size: 31px;
  }
  .duration .date-blank {
    display: inline-block;
    width: 132px;
    border-bottom: 1px solid var(--rule);
    vertical-align: baseline;
    height: 1px;
    margin-left: 2px;
  }
  .signature {
    position: absolute;
    top: 743px;
    border-top: 1px solid var(--rule);
    font-family: "Pinyon Script", cursive;
    font-size: 27px;
    color: var(--ink);
    padding-top: 2px;
    text-align: left;
  }
  .signature.cert-no { left: 10px; width: 151px; }
  .signature.officer { left: 377px; width: 273px; }
</style>
</head>
<body>
<main class="certificate">
  <svg class="frame-lines" width="1200" height="846" viewBox="0 0 1200 846" aria-hidden="true">
    <g stroke="#dbb55e" stroke-width="2.6" fill="none">
      <line x1="57" y1="11.5" x2="1142" y2="11.5"/>
      <line x1="63" y1="23" x2="1136" y2="23"/>
      <line x1="57" y1="833" x2="1142" y2="833"/>
      <line x1="63" y1="821.5" x2="1136" y2="821.5"/>
      <line x1="11.5" y1="57" x2="11.5" y2="789"/>
      <line x1="22" y1="63" x2="22" y2="783"/>
      <line x1="1188.5" y1="57" x2="1188.5" y2="789"/>
      <line x1="1178" y1="63" x2="1178" y2="783"/>
    </g>
  </svg>
  <div class="corner-flourish tl" role="img" aria-label="Gold corner flourish"></div>
  <div class="corner-flourish tr" role="img" aria-label="Gold corner flourish"></div>
  <div class="corner-flourish bl" role="img" aria-label="Gold corner flourish"></div>
  <div class="corner-flourish br" role="img" aria-label="Gold corner flourish"></div>

  <aside class="brand-band">
    <p class="brand-name"><span class="line-1">ØSTRA</span><span class="line-2">VELMARK</span></p>
  </aside>

  <section class="content">
    <h1 class="title">CERTIFICATE OF COMPLETION</h1>
    <p class="lead awarded">This certificate is awarded to</p>
    <div class="recipient-line"></div>
    <p class="lead completed">has successfully completed</p>
    <h2 class="course">Customer Relation Management</h2>
    <p class="duration">16 hours training course held on<span class="date-blank"></span></p>
    <p class="signature cert-no">Certificate No.</p>
    <p class="signature officer">Chief Technology Officer</p>
  </section>
</main>
</body>
</html>
```